Coffee Package Design

We need a new package design for a coffee company. Need to be a mix between modern and classic design combined together. We are open to different ideas.
We changing our product name from Café Verlona to Café Rostelli. The picture upload
shows what the product looks like. We want something completely different. The name of the company should go on the back of the package.
Updates

Hello Everyone,

Please read description, we are going with a new name and design for the product.

Café Rostelli. Café Verlona is what we are replacing with Café Rostelli, we are looking for new

look and design, please submit new designs.

There is a change in the description. Please take out Premium coffee blend and replace with Italian Roast.                                    

Industry/Entity Type

Cafe

Requirements
Must have
• You can use up to 6 colors.
Please put these items on design: Café Rostelli (this is the product name), Regular Premium Blend Coffee, 100% Arabica,
Dumbrell & Sons (name of the company), Tyler, TX on the back of the package

The file uploaded is an example of one of our products and how the package film
is sized.

```html
<!DOCTYPE html>
<html lang="en">
<head>
<meta charset="UTF-8">
<title>Café Rostelli – Italian Roast Package</title>
<link rel="stylesheet" href="https://fonts.googleapis.com/css2?family=Barlow:wght@300;700&family=Dancing+Script:wght@600&family=Tinos&display=swap">
<style>
  :root {
    --film-dark: #7c7d80;
    --film-mid: #9a9b9e;
    --film-light: #b9babd;
    --ink-white: #ffffff;
    --ink-black: #1c1c1c;
    --roast-red: #ee4a36;
    --roast-red-deep: #c93424;
    --art-tone-a: #5f9a7c;
    --art-tone-b: #b7a8a2;
  }
  * { margin: 0; padding: 0; box-sizing: border-box; }
  html, body {
    width: 1200px;
    height: 1000px;
    overflow: hidden;
  }
  .package-face {
    position: relative;
    width: 1200px;
    height: 1000px;
    background: linear-gradient(100deg, var(--film-dark) 0%, var(--film-mid) 30%, var(--film-light) 55%, var(--film-mid) 78%, var(--film-dark) 100%);
    overflow: hidden;
  }
  .brand-cafe {
    position: absolute;
    top: 140px;
    left: 0;
    width: 100%;
    padding-right: 190px;
    text-align: center;
    font-family: "Dancing Script", cursive;
    font-weight: 600;
    font-size: 118px;
    line-height: 1;
    color: var(--ink-black);
    transform: rotate(-4deg);
  }
  .brand-name {
    position: absolute;
    top: 252px;
    left: 0;
    width: 100%;
    text-align: center;
    font-family: "Barlow", sans-serif;
    font-weight: 700;
    font-size: 150px;
    line-height: 1;
    letter-spacing: 2px;
    color: var(--ink-white);
  }
  .roast-ribbon {
    position: absolute;
    top: 424px;
    left: 370px;
    width: 460px;
    height: 62px;
  }
  .roast-ribbon svg {
    position: absolute;
    inset: 0;
  }
  .roast-ribbon-label {
    position: relative;
    display: block;
    text-align: center;
    font-family: "Tinos", serif;
    font-size: 40px;
    line-height: 62px;
    letter-spacing: 2px;
    color: var(--ink-white);
  }
  .scooter-art {
    position: absolute;
    top: 512px;
    left: 440px;
    width: 320px;
    height: 296px;
    border-radius: 8px;
    background: linear-gradient(135deg, var(--art-tone-a) 0%, var(--art-tone-b) 100%);
  }
  .product-claims {
    position: absolute;
    top: 830px;
    left: 0;
    width: 100%;
    text-align: center;
    font-family: "Barlow", sans-serif;
    font-weight: 300;
    font-size: 44px;
    line-height: 1.25;
    color: var(--ink-white);
  }
</style>
</head>
<body>
  <main class="package-face">
    <div class="brand-cafe">café</div>
    <h1 class="brand-name">ROSTELLI</h1>

    <div class="roast-ribbon">
      <svg width="460" height="62" viewBox="0 0 460 62" aria-hidden="true">
        <polygon points="0,0 460,0 440,31 460,62 0,62 20,31" fill="var(--roast-red)"/>
        <polygon points="0,0 12,0 12,62 0,62 20,31" fill="var(--roast-red-deep)"/>
        <polygon points="460,0 448,0 448,62 460,62 440,31" fill="var(--roast-red-deep)"/>
      </svg>
      <span class="roast-ribbon-label">ITALIAN ROAST</span>
    </div>

    <div class="scooter-art" role="img" aria-label="Illustration area: vintage scooter silhouette emblem"></div>

    <p class="product-claims">FRESHLY ROASTED &amp; PACKED<br>100% ARABICA COFFEE</p>
  </main>
</body>
</html>
```